TAILWIND FIELDS Pet Resorts Outdoor Signage

4 x 8 outdoor signage design for our two locations

Target Market(s)

Existing and New Customers

Industry/Entity Type

Pet Care

Font styles to use
Sans Serif

Colors

Designer to choose colors to be used in the design.

```html
<!DOCTYPE html>
<html lang="en">
<head>
<meta charset="utf-8">
<title>TAILWIND FIELDS Pet Resorts – Outdoor Signage</title>
<link rel="stylesheet" href="https://fonts.googleapis.com/css2?family=Open+Sans:wght@300;400;700;800&display=swap">
<style>
  :root{
    --teal:#1ba3a3;
    --charcoal:#474747;
    --paper:#f4f4f4;
    --paper-shade:#e6e6e6;
    --white:#ffffff;
    --backdrop:#cfcfcf;
  }
  *{margin:0;padding:0;box-sizing:border-box}
  html,body{width:1200px;height:1200px;overflow:hidden}
  body{background:var(--backdrop);font-family:"Open Sans",sans-serif;position:relative}
  .sign{position:absolute;top:219px;width:401px;height:801px;background:linear-gradient(160deg,var(--white),var(--paper-shade));overflow:hidden}
  .sign--resort{left:169px}
  .sign--campus{left:630px}
  .sign__bands{position:absolute;inset:0;width:100%;height:100%}
  .brand-name{position:absolute;left:0;right:0;text-align:center;color:var(--charcoal);font-weight:800;line-height:.95;letter-spacing:-1px}
  .sign--resort .brand-name{top:110px;font-size:58px}
  .sign--campus .brand-name{top:120px;font-size:50px}
  .headline{position:absolute;left:0;right:0;text-align:center;color:var(--white);font-weight:800;letter-spacing:.5px}
  .sign--resort .headline{top:440px;font-size:54px;line-height:56px}
  .sign--campus .headline{top:437px;font-size:45px;line-height:41px}
  .rule{position:absolute;left:50px;width:301px;top:577px;height:1px;background:linear-gradient(90deg,transparent,var(--white),transparent)}
  .tagline{position:absolute;left:0;right:0;text-align:center;color:var(--white);top:598px}
  .tagline__lead{display:block;font-weight:300;font-size:30px;line-height:34px;letter-spacing:.5px}
  .tagline__main{display:block;font-weight:800;font-size:44px;line-height:46px}
  .services{position:absolute;top:585px;left:0;right:0;height:95px}
  .service{position:absolute;width:110px;margin-left:-55px;text-align:center}
  .service:nth-child(1){left:75px}
  .service:nth-child(2){left:199px}
  .service:nth-child(3){left:322px}
  .service__badge{display:block;width:72px;height:60px;margin:0 auto}
  .service__label{display:block;color:var(--white);font-weight:700;font-size:17px;margin-top:8px}
  .service:nth-child(1) .service__label{margin-top:4px}
  .divider{position:absolute;top:600px;width:2px;height:60px;background:var(--white)}
  .divider--a{left:137px}
  .divider--b{left:260px}
  .contact{position:absolute;left:0;right:0;top:726px;text-align:center;color:var(--white)}
  .contact__phone{display:flex;align-items:center;justify-content:center;gap:8px;font-weight:800;font-size:32px;line-height:38px}
  .contact__phone svg{width:28px;height:28px}
  .contact__web{display:flex;align-items:center;justify-content:center;gap:10px;font-size:18px;line-height:22px;margin-top:2px}
  .contact__web svg{width:13px;height:13px}
  .contact__web b{font-weight:700}
</style>
</head>
<body>

<svg width="0" height="0" style="position:absolute">
  <defs>
    <symbol id="icon-phone" viewBox="0 0 24 24"><path fill="currentColor" d="M6.6 10.8a15.2 15.2 0 0 0 6.6 6.6l2.2-2.2c.3-.3.7-.4 1-.2 1.1.4 2.3.6 3.6.6.6 0 1 .4 1 1V20c0 .6-.4 1-1 1A17 17 0 0 1 3 4c0-.6.4-1 1-1h3.5c.6 0 1 .4 1 1 0 1.3.2 2.5.6 3.6.1.3 0 .7-.2 1z"/><path fill="none" stroke="currentColor" stroke-width="1.8" stroke-linecap="round" d="M14 3.5a7 7 0 0 1 6.5 6.5M14 7a3.5 3.5 0 0 1 3 3"/></symbol>
    <symbol id="icon-globe" viewBox="0 0 24 24"><g fill="none" stroke="currentColor" stroke-width="1.6"><circle cx="12" cy="12" r="10"/><ellipse cx="12" cy="12" rx="4.5" ry="10"/><path d="M2 12h20M4 7h16M4 17h16"/></g></symbol>
    <symbol id="badge-blob" viewBox="0 0 72 60"><path fill="#3d3d3d" d="M14 8c10-9 30-7 40 4s14 26 4 36-34 12-46 2S4 17 14 8z"/><path fill="#ffffff" d="M22 6c12-6 30 0 38 12s8 26-4 32-30 6-42 0S4 26 10 18 14 10 22 6z"/></symbol>
  </defs>
</svg>

<section class="sign sign--resort">
  <svg class="sign__bands" viewBox="0 0 646 1290" preserveAspectRatio="none" aria-hidden="true">
    <polygon points="0,700 646,432 646,508" fill="#474747"/>
    <polygon points="0,708 646,520 646,1148 0,1148" fill="#1ba3a3"/>
    <rect x="0" y="1156" width="646" height="134" fill="#474747"/>
  </svg>
  <div class="brand-name">TAILWIND<br>FIELDS</div>
  <h2 class="headline">ALL BREED<br>FRIENDLY</h2>
  <div class="services">
    <div class="service"><svg class="service__badge" role="img" aria-label="Boarding icon: house with paw print"><use href="#badge-blob"/></svg><span class="service__label">Boarding</span></div>
    <div class="service"><svg class="service__badge" role="img" aria-label="Daycare icon: person walking a dog in the sun"><use href="#badge-blob"/></svg><span class="service__label">Daycare</span></div>
    <div class="service"><svg class="service__badge" role="img" aria-label="Training icon: trainer with a jumping dog"><use href="#badge-blob"/></svg><span class="service__label">Training</span></div>
  </div>
  <span class="divider divider--a"></span>
  <span class="divider divider--b"></span>
  <div class="contact">
    <div class="contact__phone"><svg><use href="#icon-phone"/></svg>905-555-0142</div>
    <div class="contact__web"><svg><use href="#icon-globe"/></svg><span>www.<b>tailwindfields</b>.ca</span></div>
  </div>
</section>

<section class="sign sign--campus">
  <svg class="sign__bands" viewBox="0 0 646 1290" preserveAspectRatio="none" aria-hidden="true">
    <polygon points="0,700 646,432 646,508" fill="#474747"/>
    <polygon points="0,708 646,520 646,1148 0,1148" fill="#1ba3a3"/>
    <rect x="0" y="1156" width="646" height="134" fill="#474747"/>
  </svg>
  <div class="brand-name">TAILWIND<br>FIELDS</div>
  <h2 class="headline">CEDAR<br>HOLLOW<br>CAMPUS</h2>
  <span class="rule"></span>
  <p class="tagline"><span class="tagline__lead">HOME TO THE</span><span class="tagline__main">SOCIAL CLUB</span></p>
  <div class="contact">
    <div class="contact__phone"><svg><use href="#icon-phone"/></svg>437-555-0187</div>
    <div class="contact__web"><svg><use href="#icon-globe"/></svg><span>www.<b>tailwindfields</b>.ca</span></div>
  </div>
</section>

</body>
</html>
```